Home Automation Business needs captivating Flyer design to get Home Owners attention

We need a Flyer designed for a new company entering the Home Automation Business.
The Flyer must have visual impact from the second it’s picked up. Whether it’s the use of colour, or wording like READ ME! or something similar that grabs the attention, it’s absolutely essential that our marketing material does not end up being immediately thrown away when someone opens their letter box and picks up the flyer.
The flyer needs to quickly let the reader know that this is information regarding Home Automation.
The flyer needs to tie together in some way with our business card so that it looks coherent and from the same organization.
The background could maybe be a house overlaid with a printed circuit board design or something that identifies with electronic technology or connection of devices in the home.
Selling Points to put on the flyer:
Home Automation.. The possibilities are limitless..
Would you like to be able to control the lighting in your home conveniently and automatically..? For example;
• Turn on your lighting when you are away or when a door or window is opened, or when motion is detected, to deter potential thieves.
• Dim your lighting for best effect when watching a favourite movie or program.
• Time control the lighting in your children room.
• Time control your hall way lighting so it’s on when you first wake up.
• Alter the colour of your kitchen LED lighting to suit your mood.
Left the house and wonder if your security system is armed or have no security system? No problem;
• The system motion sensor will report movement and email you that someone is in your house.
• The same motion sensor can be used to detect rising temperature; Place one in any important area to alert you to the conditions in the room. The sensor also monitors light level and can be used to turn on exterior lighting as darkness falls.
• Integrate IP based cameras for a total solution.
Worried about flooding?
• A flood sensor can alert you to potentially costly water damage.
Devices can be connected to a central base unit by J-Lumo technology..-There are no intrusive wires and the central base unit connects to your internet router so that you are in control wherever you are.
Home Automation can add real value to your house.

Reason: Hi guys, Just a bit more time to get some more awesome designs. Thank you

Target Market(s)

Home Owner

Industry/Entity Type

Home And Garden

Font styles to use
Sans Serif

Colors
f37122

Requirements
Must have
• Must be capture readers attention before its thrown away.
Nice to have
• Must tie into our Mockup hive designed business card
Should not have
• We don't have any particular Not Haves at this stage..

```html
<!DOCTYPE html>
<html lang="en">
<head>
<meta charset="utf-8">
<title>Home Automation Flyer</title>
<link href="https://fonts.googleapis.com/css2?family=Raleway:wght@600;700;800&display=swap" rel="stylesheet">
<style>
  :root {
    --ink-dark: #333333;
    --circuit-glow: #4a5d6b;
    --circuit-mid: #3a4650;
    --accent: #f37122;
    --text-light: #ffffff;
  }
  * { margin: 0; padding: 0; box-sizing: border-box; }
  html, body { width: 850px; height: 1200px; overflow: hidden; background: var(--ink-dark); }
  .flyer {
    position: relative;
    width: 850px;
    height: 1200px;
    overflow: hidden;
    font-family: "Raleway", sans-serif;
    color: var(--text-light);
  }
  .circuit-backdrop {
    position: absolute;
    inset: 0;
    background:
      radial-gradient(ellipse 55% 45% at 50% 48%, var(--circuit-glow) 0%, var(--circuit-mid) 45%, transparent 80%),
      var(--ink-dark);
  }
  .heading {
    position: absolute;
    left: 80px;
    width: 700px;
    color: var(--accent);
    font-weight: 700;
    font-size: 19.5px;
    line-height: 25px;
    letter-spacing: 0.2px;
  }
  .point {
    position: absolute;
    left: 80px;
    width: 700px;
    font-weight: 700;
    font-size: 15.5px;
    line-height: 21px;
    letter-spacing: 0.3px;
  }
  .closing {
    position: absolute;
    left: 0;
    width: 850px;
    top: 1044px;
    text-align: center;
    color: var(--accent);
    font-weight: 700;
    font-size: 35px;
    line-height: 43px;
    letter-spacing: 0.8px;
  }
</style>
</head>
<body>
<main class="flyer">
  <div class="circuit-backdrop" role="img" aria-label="Dark background with a glowing blue printed circuit board pattern"></div>

  <h2 class="heading" style="top:46px">Would you like to be able to control the lighting in your home<br>&nbsp;conveniently and automatically..? For example;</h2>
  <p class="point" style="top:114px;left:82px">Turn on your lighting when you are away or when a door or window is opened, or when motion is detected, to deter potential thieves.</p>
  <p class="point" style="top:175px;left:82px">Dim your lighting for best effect when watching a favourite movie or program.</p>
  <p class="point" style="top:233px">Time control the lighting in your children room.</p>
  <p class="point" style="top:274px;left:82px">Time control your hall way lighting so it’s on when you first wake up.</p>
  <p class="point" style="top:308px;left:82px">Alter the colour of your kitchen LED lighting to suit your mood.</p>

  <h2 class="heading" style="top:441px">Left the house and wonder if your security system is armed or have no security system? No problem;</h2>
  <p class="point" style="top:510px">The system motion sensor will report movement and email you that someone is in your house.</p>
  <p class="point" style="top:572px">The same motion sensor can be used to detect rising temperature; Place one in any important area to alert you to the conditions in the room. The sensor also monitors light level and can be used to turn on exterior lighting as darkness falls.</p>
  <p class="point" style="top:677px">Integrate IP based cameras for a total solution.</p>

  <h2 class="heading" style="top:799px">Worried about flooding?</h2>
  <p class="point" style="top:844px;left:82px">A flood sensor can alert you to potentially costly water damage.</p>
  <p class="point" style="top:888px">Devices can be connected to a central base unit by J-Lumo technology..- There are no intrusive wires and the central base unit connects to your internet router so that you are in control wherever you are.</p>

  <h1 class="closing">Home Automation Can Add Real Value To<br>Your House</h1>
</main>
</body>
</html>
```